Apartment Investor Business Card Design

Need a new business card designed for my multifamily investment company

Industry/Entity Type

Real Estate

Contact Information for Business Card

Garrick Pelham - President & CEO
Brightwold Holdings, LLC
4838 North 92nd Avenue, Ste 500
Omaha, NE 68999
(402) 555-0147
Garrick@brightwoldholdings.example
Www.BrightwoldHoldings.example

Colors
3176b5

```html
<!DOCTYPE html>
<html lang="en">
<head>
<meta charset="utf-8">
<title>Brightwold Holdings – Business Card</title>
<link rel="stylesheet" href="https://fonts.googleapis.com/css2?family=Exo+2:wght@400;500;600;700&display=swap">
<style>
  :root {
    --brand-blue: #3176b5;
    --back-blue: #4f86c6;
    --ink: #1c1c1c;
    --paper: #ffffff;
    --stage: #ecebe8;
  }
  * { box-sizing: border-box; margin: 0; padding: 0; }
  html, body {
    width: 1200px; height: 900px; overflow: hidden;
    background: var(--stage);
    font-family: "Exo 2", sans-serif;
  }
  .canvas { position: relative; width: 1200px; height: 900px; }
  .card {
    position: absolute; left: 290px;
    width: 620px; height: 354px;
    border-radius: 18px; overflow: hidden;
    box-shadow: 0 6px 18px rgba(0,0,0,.15);
  }
  .card--back { top: 60px; background: var(--back-blue); display: flex; align-items: center; justify-content: center; }
  .card--front { top: 480px; background: var(--paper); }

  .brand-mark { display: flex; align-items: center; gap: 12px; font-weight: 500; letter-spacing: .04em; text-transform: uppercase; }
  .brand-mark__dot { width: 14px; height: 14px; flex: none; }
  .card--back .brand-mark { color: var(--paper); font-size: 34px; }
  .card--back .brand-mark__dot { background: var(--paper); }
  .card--front .brand-mark { position: absolute; left: 34px; top: 140px; color: var(--ink); font-size: 21px; }
  .card--front .brand-mark__dot { background: var(--brand-blue); }

  .contact { position: absolute; left: 328px; top: 64px; }
  .contact__name { font-size: 27px; font-weight: 600; color: var(--ink); letter-spacing: .02em; }
  .contact__name .first { color: var(--brand-blue); }
  .contact__title { font-size: 15px; font-weight: 600; color: var(--ink); margin-top: 2px; }
  .contact__title .company { color: var(--brand-blue); }
  .contact__list { list-style: none; margin-top: 18px; }
  .contact__item { display: flex; align-items: center; gap: 14px; font-size: 15px; color: var(--ink); height: 28px; }
  .contact__item svg { width: 16px; height: 16px; fill: var(--brand-blue); flex: none; }

  .address-band {
    position: absolute; left: 0; right: 0; bottom: 48px; height: 42px;
    background: var(--brand-blue); color: var(--paper);
    display: flex; align-items: center; padding-left: 34px;
    font-size: 17px; letter-spacing: .03em;
  }
</style>
</head>
<body>
<main class="canvas">
  <section class="card card--back">
    <div class="brand-mark"><span class="brand-mark__dot"></span>Brightwold Holdings</div>
  </section>

  <section class="card card--front">
    <div class="brand-mark"><span class="brand-mark__dot"></span>Brightwold Holdings</div>

    <div class="contact">
      <h1 class="contact__name"><span class="first">Garrick</span> Pelham</h1>
      <p class="contact__title">President &amp; CEO of <span class="company">Brightwold Holdings</span></p>
      <ul class="contact__list">
        <li class="contact__item">
          <svg viewBox="0 0 24 24" aria-hidden="true"><path d="M6.6 10.8a15 15 0 0 0 6.6 6.6l2.2-2.2c.3-.3.7-.4 1-.2 1.1.4 2.3.6 3.6.6.6 0 1 .4 1 1V20c0 .6-.4 1-1 1A17 17 0 0 1 3 4c0-.6.4-1 1-1h3.5c.6 0 1 .4 1 1 0 1.3.2 2.5.6 3.6.1.3 0 .7-.2 1z"/></svg>
          (402) 555-0147
        </li>
        <li class="contact__item">
          <svg viewBox="0 0 24 24" aria-hidden="true"><path d="M12 2a10 10 0 1 0 0 20 10 10 0 0 0 0-20zm6.9 6h-3a15 15 0 0 0-1.3-3.9A8 8 0 0 1 18.9 8zM12 4c.8 1.2 1.5 2.5 1.9 4h-3.8c.4-1.5 1.1-2.8 1.9-4zM4.3 14a8 8 0 0 1 0-4h3.4a16 16 0 0 0 0 4zm.8 2h3a15 15 0 0 0 1.3 3.9A8 8 0 0 1 5.1 16zm3-8h-3a8 8 0 0 1 4.3-3.9A15 15 0 0 0 8.1 8zM12 20c-.8-1.2-1.5-2.5-1.9-4h3.8c-.4 1.5-1.1 2.8-1.9 4zm2.3-6H9.7a14 14 0 0 1 0-4h4.6a14 14 0 0 1 0 4zm.3 5.9c.6-1.2 1-2.5 1.3-3.9h3a8 8 0 0 1-4.3 3.9zM16.3 14a16 16 0 0 0 0-4h3.4a8 8 0 0 1 0 4z"/></svg>
          www.brightwoldholdings.example
        </li>
        <li class="contact__item">
          <svg viewBox="0 0 24 24" aria-hidden="true"><path d="M2 5h20v14H2zm2 2v.5l8 5 8-5V7zm0 2.8V17h16V9.8l-8 5z"/></svg>
          garrick@brightwoldholdings.example
        </li>
      </ul>
    </div>

    <div class="address-band">4838 North 92nd Avenue, Ste 500, Omaha, NE 68999</div>
  </section>
</main>
</body>
</html>
```